Wellbeing Challenge Posters

We are running a wellbeing challenge. Every week we run a challenge under a different theme. We need 5 themes to start with:
- Connect
- Be mindful
- Get moving
- Give
- Grow your mind

Each theme needs to have the following:
1. Match the colours of the icons provided under each
2. Have a clear place for the word where these can be changed but utilising the same theme. For example, under connect, we will run a number of different challenges but the theme will remain the same.
3. Each theme will have the following:
-This week's challenge
- Points
4. The Thrive Week logo

The content under each of the themes will be as follows:

1. Connect
This week's challenge: Have a shared meal with your team - take a photo and post it on the challenge forum
Points: 10 points per person that attended if you had more than 75% of your team

2. Be Mindful
This week's challenge: START something that will improve your wellbeing, STOP something that is bad for you - Be mindful of how you feel at the end of the week.

3. Get moving:
This week's challenge: Do a minimum 150 minutes of exercise this week required for good general health - try something new!
Points: Take your usual 1 point per 30 mins exercise but give yourself an additional 10 points if you do 150mins or more for the week.

4. Give:
This week's challenge: Do a random act of kindness every day this week
Points: 1 point per day PLUS 10 points if you complete 1 every day

5. Grow Your Mind
This week's challenge: Learn something new every day! Read a research paper, watch a KAV talk, DIY, learn something about your workmates

```html
<!DOCTYPE html>
<html lang="en">
<head>
<meta charset="utf-8">
<title>Give – Be there for others</title>
<link rel="stylesheet" href="https://fonts.googleapis.com/css2?family=Bebas+Neue&family=Ubuntu:wght@400;500;700&family=Roboto+Slab:wght@800&display=swap">
<style>
  :root {
    --pink: #ec1c7a;
    --pink-mid: #f05a94;
    --pink-soft: #f6a9c6;
    --pink-pale: #fde6ef;
    --teal: #19a8b4;
    --lime: #c2d957;
    --ink: #4a4a4a;
    --grey: #5d5d5d;
    --sky: #9fd2dc;
    --white: #ffffff;
  }
  * { box-sizing: border-box; margin: 0; padding: 0; }
  html, body { width: 987px; height: 1200px; overflow: hidden; background: var(--white); }
  .poster {
    position: relative; width: 987px; height: 1200px; overflow: hidden;
    background: linear-gradient(180deg, var(--pink) 0%, var(--pink-mid) 28%, var(--pink-soft) 52%, var(--pink-pale) 64%, var(--white) 72%);
    font-family: "Ubuntu", sans-serif;
  }
  .theme-word {
    position: absolute; top: 80px; left: 0; width: 100%; text-align: center;
    font-family: "Roboto Slab", serif; font-weight: 800; font-size: 150px; letter-spacing: 4px;
    color: var(--white); line-height: 1; transform: scaleX(0.78);
  }
  .theme-icon { position: absolute; left: 337px; top: 228px; width: 328px; height: 277px; }
  .tagline {
    position: absolute; top: 512px; left: 0; width: 100%; text-align: center;
    font-size: 58px; font-weight: 500; color: var(--teal); line-height: 1.1;
  }
  .challenge-ribbon { position: absolute; left: 63px; top: 608px; width: 856px; height: 66px; }
  .challenge-ribbon span {
    position: absolute; inset: 0; display: flex; align-items: center; justify-content: center;
    font-family: "Bebas Neue", sans-serif; font-size: 60px; letter-spacing: 1px; color: var(--white);
    padding-top: 4px;
  }
  .challenge-text {
    position: absolute; top: 694px; left: 0; width: 100%; text-align: center;
    font-size: 36px; line-height: 45px; color: var(--ink);
  }
  .points-box {
    position: absolute; left: 111px; top: 842px; width: 768px; height: 151px;
    border: 3px solid var(--teal); border-top: none;
  }
  .points-box::before, .points-box::after {
    content: ""; position: absolute; top: 0; height: 3px; background: var(--teal);
  }
  .points-box::before { left: -3px; width: 262px; }
  .points-box::after { right: -3px; width: 262px; }
  .points-title {
    position: absolute; top: -22px; left: 0; width: 100%; text-align: center;
    font-family: "Bebas Neue", sans-serif; font-weight: 400; font-size: 56px; color: var(--teal); line-height: 1;
  }
  .points-text {
    position: absolute; top: 40px; left: 0; width: 100%; text-align: center;
    font-size: 40px; line-height: 44px; color: var(--lime); letter-spacing: 1px;
  }
  .contact-band { position: absolute; left: 0; top: 1063px; width: 620px; height: 137px; }
  .contact { position: absolute; left: 24px; top: 1080px; color: var(--white); }
  .contact h2 {
    font-family: "Bebas Neue", sans-serif; font-weight: 400; font-size: 37px; line-height: 1;
  }
  .contact p { display: flex; align-items: center; gap: 12px; font-size: 22px; margin-top: 8px; }
  .contact svg { width: 26px; height: 26px; }
  .brand {
    position: absolute; left: 640px; width: 320px; top: 1108px; text-align: center;
    font-family: "Ubuntu", sans-serif; font-weight: 700; font-size: 32px; color: var(--grey);
  }
</style>
</head>
<body>
<main class="poster">
  <h1 class="theme-word">GIVE</h1>

  <div class="theme-icon" role="img" aria-label="Theme icon: two figures embracing, in orange, teal and lime">
    <svg viewBox="0 0 328 277" width="328" height="277">
      <rect x="0" y="0" width="328" height="277" rx="120" fill="#ffffff"/>
      <rect x="14" y="14" width="300" height="249" rx="110" fill="#c2d957"/>
    </svg>
  </div>

  <p class="tagline">Be there for others</p>

  <div class="challenge-ribbon">
    <svg viewBox="0 0 856 66" width="856" height="66" preserveAspectRatio="none">
      <polygon points="0,0 856,0 842,33 856,66 0,66 14,33" fill="var(--lime)"/>
    </svg>
    <span>THIS WEEK'S CHALLENGE</span>
  </div>

  <p class="challenge-text">Do a random act<br>of kindness every day this week</p>

  <section class="points-box">
    <h2 class="points-title">POINTS</h2>
    <p class="points-text">1 point per day PLUS 10 points<br>if you complete 1 every day</p>
  </section>

  <svg class="contact-band" viewBox="0 0 620 137" width="620" height="137">
    <polygon points="510,0 528,0 620,137 600,137" fill="var(--sky)"/>
    <polygon points="0,0 510,0 588,137 0,137" fill="var(--lime)"/>
  </svg>
  <div class="contact">
    <h2>CONTACT US NOW TO REGISTER YOUR TEAM</h2>
    <p>
      <svg viewBox="0 0 26 26"><circle cx="13" cy="13" r="13" fill="#fff"/><path d="M9 7l3 3-1.5 1.8c.8 1.6 2 2.8 3.7 3.7L16 14l3 3-1.6 2c-4.6-.4-8.7-4.5-9.3-9.3z" fill="var(--lime)"/></svg>
      04 555 0192
    </p>
    <p>
      <svg viewBox="0 0 26 26"><circle cx="13" cy="13" r="13" fill="#fff"/><circle cx="13" cy="13" r="7" fill="none" stroke="var(--lime)" stroke-width="1.5"/><path d="M6 13h14M13 6c-3 4-3 10 0 14M13 6c3 4 3 10 0 14" fill="none" stroke="var(--lime)" stroke-width="1.5"/></svg>
      thriveweekteams.co.nz
    </p>
  </div>

  <div class="brand">The Thrive Week</div>
</main>
</body>
</html>
```